Brivane Computing business card with new logo design for HPC Software Engineer

We are start up company based in Singapore focusing on high performance computing (HPC) software technology. We perform software performance analysis, and optimize software performance for multi-core CPU and GPU.

High Performance Computing (HPC) has the core spirit of appreciating precious time, and being green and efficient. We like to have green color theme business card and logo design.

See our current website for more information: http://www.brivanecomputing.example
Also attached current business card for reference only.

The business card should include the following information:
Chinese Name: 潘立衡
English Name: Pan Lai Heng
Email: mayrel@brivanecomputing.example
Job title: HPC Software Engineer
Certification: Torvex Certified LUMA Programmer
Office phone: (65) 6120 7359
Mobile phone: (65) 9214 0563

Chinese Idiom: 一寸光陰 一寸金,寸金難買 寸光陰。
English translate of the idiom above: An inch of time, an inch of gold. An inch of gold could not buy an inch of time.

Target Market(s)

Professionals in IT

Industry/Entity Type

Computer Software

Contact Information for Business Card

Company name: Brivane Computing

Chinese Name: 潘立衡

Font styles to use
Serif
Sans Serif

```html
<!DOCTYPE html>
<html lang="en">
<head>
<meta charset="utf-8">
<title>Brivane Computing – Business Card</title>
<link rel="stylesheet" href="https://fonts.googleapis.com/css2?family=Alegreya:wght@700&family=Montserrat:wght@700&family=Open+Sans:wght@400&family=Noto+Sans+TC:wght@400&display=swap">
<style>
  :root {
    --bg: #3b3b3b;
    --white: #ffffff;
    --green-dark: #1f5a3f;
    --green-mid: #2f6f4a;
    --green-light: #4caf47;
    --text-grey: #5a5a5a;
    --cert-green: #2e6b4c;
  }
  * { margin: 0; padding: 0; box-sizing: border-box; }
  html, body { width: 1200px; height: 1200px; overflow: hidden; background: var(--bg); }
  .canvas { position: relative; width: 1200px; height: 1200px; }

  .card { position: absolute; left: 170px; width: 872px; height: 485px; overflow: hidden; }

  /* Front */
  .card-front { top: 85px; background: var(--white); }
  .brand-front {
    position: absolute; right: 48px; top: 140px;
    display: flex; align-items: center; gap: 14px;
    font-family: "Alegreya", Georgia, serif; font-weight: 700;
    font-size: 42px; color: var(--green-dark);
  }
  .brand-mark { width: 26px; height: 26px; background: var(--green-light); }
  .name-zh {
    position: absolute; left: 57px; top: 193px;
    font-family: "Noto Sans TC", sans-serif; font-size: 30px; color: var(--green-dark);
  }
  .name-en {
    position: absolute; left: 48px; top: 236px;
    font-family: "Montserrat", Arial, sans-serif; font-weight: 700;
    font-size: 32px; color: var(--green-dark);
  }
  .job-title {
    position: absolute; left: 48px; top: 280px;
    font-family: "Open Sans", Arial, sans-serif; font-size: 19px; color: var(--text-grey);
  }
  .divider {
    position: absolute; left: 47px; top: 317px; width: 777px; height: 2px;
    background: var(--green-mid);
  }
  .contact-list {
    position: absolute; left: 47px; top: 339px; list-style: none;
    font-family: "Open Sans", Arial, sans-serif; font-size: 19px; color: var(--text-grey);
  }
  .contact-list li { display: flex; align-items: center; gap: 9px; height: 30.5px; }
  .contact-list svg { width: 19px; height: 19px; fill: var(--green-light); flex: none; }
  .certification {
    position: absolute; right: 48px; top: 339px; text-align: right;
    font-family: "Open Sans", Arial, sans-serif; font-size: 19px; line-height: 30.5px;
    color: var(--text-grey);
  }
  .certification .label { color: var(--cert-green); }
  .footer-band {
    position: absolute; left: 0; bottom: 0; width: 100%; height: 37px;
    background: var(--green-dark);
  }
  .footer-accent-gap {
    position: absolute; left: 348px; bottom: 20px; width: 530px; height: 20px;
    background: var(--white); border-top-left-radius: 10px;
  }
  .footer-accent {
    position: absolute; left: 354px; bottom: 19px; width: 520px; height: 16px;
    background: var(--green-light); border-top-left-radius: 8px;
  }
  .website {
    position: absolute; left: 47px; bottom: 8px;
    font-family: "Open Sans", Arial, sans-serif; font-size: 19px; color: var(--white);
  }

  /* Back */
  .card-back {
    top: 633px;
    background: linear-gradient(125deg, #1e5a3d 0%, #2c7045 45%, #4b9f48 100%);
  }
  .brand-back {
    position: absolute; left: 0; right: 0; top: 268px; text-align: center;
    font-family: "Alegreya", Georgia, serif; font-weight: 700;
    font-size: 44px; color: var(--white);
  }
  .idiom {
    position: absolute; left: 0; right: 0; top: 380px; text-align: center;
    color: var(--white); font-size: 19px; line-height: 31px;
  }
  .idiom .zh { font-family: "Noto Sans TC", sans-serif; }
  .idiom .en { font-family: "Open Sans", Arial, sans-serif; }
</style>
</head>
<body>
<main class="canvas">
  <section class="card card-front" aria-label="Business card front">
    <div class="brand-front"><span class="brand-mark"></span>Brivane Computing</div>
    <div class="name-zh">潘立衡</div>
    <div class="name-en">Pan Lai Heng</div>
    <div class="job-title">HPC Software Engineer</div>
    <div class="divider"></div>
    <ul class="contact-list">
      <li>
        <svg viewBox="0 0 24 24" aria-hidden="true"><path d="M6.6 10.8a15.1 15.1 0 0 0 6.6 6.6l2.2-2.2c.3-.3.7-.4 1-.2 1.1.4 2.3.6 3.6.6.6 0 1 .4 1 1V20c0 .6-.4 1-1 1A17 17 0 0 1 3 4c0-.6.4-1 1-1h3.5c.6 0 1 .4 1 1 0 1.3.2 2.5.6 3.6.1.3 0 .7-.2 1z"/></svg>
        (65) 6120 7359
      </li>
      <li>
        <svg viewBox="0 0 24 24" aria-hidden="true"><path d="M7 1h10a2 2 0 0 1 2 2v18a2 2 0 0 1-2 2H7a2 2 0 0 1-2-2V3a2 2 0 0 1 2-2zm0 3v14h10V4zm5 15.5a1.2 1.2 0 1 0 0 2.4 1.2 1.2 0 0 0 0-2.4z"/></svg>
        (65) 9214 0563
      </li>
      <li>
        <svg viewBox="0 0 24 24" aria-hidden="true"><path d="M2 5h20v14H2zm2 2v.4l8 5.6 8-5.6V7zm0 2.8V17h16V9.8l-8 5.6z"/></svg>
        mayrel@brivanecomputing.example
      </li>
    </ul>
    <div class="certification">
      <div class="label">Certification:</div>
      <div>Torvex Certified</div>
      <div>LUMA Programmer</div>
    </div>
    <div class="footer-band"></div>
    <div class="footer-accent-gap"></div>
    <div class="footer-accent"></div>
    <div class="website">www.brivanecomputing.example</div>
  </section>

  <section class="card card-back" aria-label="Business card back">
    <div class="brand-back">Brivane Computing</div>
    <div class="idiom">
      <div class="zh">寸光陰 一寸金, 寸金難買 寸光陰。</div>
      <div class="en">An inch of time, an inch of gold. An inch of gold could not buy an inch of time.</div>
    </div>
  </section>
</main>
</body>
</html>
```